Update our OBGYN business card look and info

We are an OBGYN office. Our logo is nice but would like to "woman" part of the logo to be a darker color, to contrast with the flower that surrounds it. Maybe make our practice name Bloom Circle Health more feminine. Our practice caters to women only. All providers and staff are female.

Target Market(s)

Females 16-65.

Industry/Entity Type

Business

Contact Information for Business Card

See attached upload. The ONLY CHANGE to the information is DELETE the name Marla Quenbright, Midwife and REPLACE with Tessa Dravinoux, Midwife

Logo Text

Bloom Circle Health Obstetrics & Gynecology

Font styles to use
Serif
Script

Colors
85cae6
0692cd
33a6d7
85abd2
f59195
eea4c8
cadf82
fac994
d3a5cc

```html
<!DOCTYPE html>
<html lang="en">
<head>
<meta charset="utf-8">
<title>Bloom Circle Health – Business Card</title>
<link href="https://fonts.googleapis.com/css2?family=Open+Sans:wght@400;600&family=Tinos:wght@400&display=swap" rel="stylesheet">
<style>
  :root {
    --stage: #0b0b0b;
    --paper: #f3f4f6;
    --brand-blue: #0692cd;
    --sky-blue: #2a96d2;
    --ink-grey: #6b6b6b;
    --soft-grey: #8a8a8a;
    --faint-mark: #e3e4e6;
    --on-blue: #ffffff;
  }
  * { margin: 0; padding: 0; box-sizing: border-box; }
  html, body { width: 1200px; height: 1000px; overflow: hidden; background: var(--stage); }
  .stage { position: relative; width: 1200px; height: 1000px; }

  .card {
    position: absolute;
    top: 350px;
    width: 510px;
    height: 300px;
    border-radius: 24px;
    overflow: hidden;
  }
  .card--front { left: 60px; background: var(--paper); }
  .card--back {
    left: 630px;
    background: linear-gradient(135deg, #3a9fd8 0%, var(--sky-blue) 55%, #1f8fcc 100%);
    display: flex; align-items: center; justify-content: center; gap: 14px;
  }

  .brand { position: absolute; left: 44px; top: 34px; display: flex; align-items: center; gap: 12px; }
  .brand__dot { width: 30px; height: 30px; border-radius: 50%; background: var(--brand-blue); }
  .brand__name {
    font-family: "Tinos", serif; font-size: 19px; letter-spacing: 0.5px;
    text-transform: uppercase; color: var(--brand-blue); line-height: 1;
  }
  .brand__tagline {
    font-family: "Open Sans", sans-serif; font-size: 14px; color: var(--ink-grey); margin-top: 4px;
  }

  .accent-tab { position: absolute; left: 0; top: 100px; width: 22px; height: 26px; background: var(--brand-blue); }

  .address {
    position: absolute; left: 44px; top: 102px;
    font-family: "Open Sans", sans-serif; font-size: 12.5px; line-height: 1.45; color: var(--ink-grey);
  }

  .contacts { position: absolute; left: 44px; top: 160px; list-style: none;
    font-family: "Open Sans", sans-serif; font-size: 12.5px; line-height: 1.55; color: var(--ink-grey); }
  .contacts li { display: flex; align-items: center; gap: 8px; }
  .contacts svg { width: 11px; height: 11px; fill: var(--brand-blue); flex: none; }

  .watermark {
    position: absolute; right: 36px; top: 110px; width: 150px; height: 150px;
    border-radius: 50%; background: var(--faint-mark);
  }

  .providers {
    position: absolute; right: 40px; top: 150px; list-style: none;
    font-family: "Tinos", serif; font-size: 17px; line-height: 1.3; color: var(--ink-grey);
  }
  .providers li { display: flex; align-items: center; gap: 9px; }
  .providers li::before {
    content: ""; width: 5px; height: 5px; border-radius: 50%; background: var(--brand-blue);
  }

  .back__dot { width: 40px; height: 40px; border-radius: 50%; background: var(--on-blue); }
  .back__name {
    font-family: "Tinos", serif; font-size: 30px; letter-spacing: 1px;
    text-transform: uppercase; color: var(--on-blue);
  }
</style>
</head>
<body>
<main class="stage">
  <section class="card card--front" aria-label="Business card front">
    <div class="brand">
      <span class="brand__dot"></span>
      <div>
        <p class="brand__name">Bloom Circle Health</p>
        <p class="brand__tagline">Obstetrics &amp; Gynecology</p>
      </div>
    </div>

    <span class="accent-tab"></span>

    <address class="address" style="font-style:normal">
      418 Linden Row<br>
      Suite 3B Harlow, GA 30944
    </address>

    <ul class="contacts">
      <li>
        <svg viewBox="0 0 24 24"><path d="M6.6 10.8a15.1 15.1 0 0 0 6.6 6.6l2.2-2.2a1 1 0 0 1 1-.25 11.4 11.4 0 0 0 3.6.57 1 1 0 0 1 1 1V20a1 1 0 0 1-1 1A17 17 0 0 1 3 4a1 1 0 0 1 1-1h3.5a1 1 0 0 1 1 1c0 1.25.2 2.45.57 3.57a1 1 0 0 1-.25 1z"/></svg>
        555 210 4836
      </li>
      <li>
        <svg viewBox="0 0 24 24"><path d="M6 3h12v5H6zM4 9h16a2 2 0 0 1 2 2v6h-4v4H6v-4H2v-6a2 2 0 0 1 2-2zm4 7v3h8v-3z"/></svg>
        555 210 4837
      </li>
      <li>
        <svg viewBox="0 0 24 24"><path d="M12 2a10 10 0 1 0 0 20 10 10 0 0 0 0-20zm6.9 6h-3a15.6 15.6 0 0 0-1.4-3.6A8 8 0 0 1 18.9 8zM12 4a14 14 0 0 1 1.9 4h-3.8A14 14 0 0 1 12 4zM4.3 14a8 8 0 0 1 0-4h3.4a16.5 16.5 0 0 0 0 4zm.8 2h3a15.6 15.6 0 0 0 1.4 3.6A8 8 0 0 1 5.1 16zm3-8h-3a8 8 0 0 1 4.4-3.6A15.6 15.6 0 0 0 8.1 8zM12 20a14 14 0 0 1-1.9-4h3.8A14 14 0 0 1 12 20zm2.3-6H9.7a14.7 14.7 0 0 1 0-4h4.6a14.7 14.7 0 0 1 0 4zm.2 5.6a15.6 15.6 0 0 0 1.4-3.6h3a8 8 0 0 1-4.4 3.6zM16.3 14a16.5 16.5 0 0 0 0-4h3.4a8 8 0 0 1 0 4z"/></svg>
        www.bloomcirclehealth.com
      </li>
    </ul>

    <span class="watermark" aria-hidden="true"></span>

    <ul class="providers">
      <li>Renata Wolsey, MD</li>
      <li>Dana Pritchell, MD</li>
      <li>Ilse Varnock, MD</li>
      <li>Tessa Dravinoux, Midwife</li>
      <li>Nora Castellane, Midwife</li>
    </ul>
  </section>

  <section class="card card--back" aria-label="Business card back">
    <span class="back__dot"></span>
    <p class="back__name">Bloom Circle Health</p>
  </section>
</main>
</body>
</html>
```